Hadley & Partners, LLC Business Card 2016

We need a new business card design for a very important trade show coming up.

We are a compliance Consulting Firm. Our clients are stock brokerage firms and investment advisers.

I would like our logo on both sides of the card.

Info in the front of the card shold include:

Logo
First & Last Name
Title
Office #
Cell #
Email
Company Address (42 W. Calloway St., Suite 300 Pasadena, CA 91417

Back of the card should include the logo and url: www.hadleypartnersgroup.com

Target Market(s)

Stock Brokerage Firms and Investment Advisers

Industry/Entity Type

Financial Service

Contact Information for Business Card

Marcus J. Pellew
President
42 W. Calloway St., Suite 300
Pasadena, CA 91417
O 626.555.0147 ext. 204
C 818.555.0193
Email: marcus@hadleypartnersgroup.com
www.hadleypartnersgroup.com

Requirements
Nice to have
• The back of the card could be black with the logo with the white letters.
• I do want the front of the card to at least have the color logo with the black "Hadley & Partners Lettering.

```html
<!DOCTYPE html>
<html lang="en">
<head>
<meta charset="utf-8">
<title>Hadley &amp; Partners — Business Card</title>
<link rel="stylesheet" href="https://fonts.googleapis.com/css2?family=Source+Sans+3:wght@400;600;700&display=swap">
<style>
  :root {
    --backdrop: #d3d4d8;
    --card-white: #ffffff;
    --card-black: #000000;
    --brand-red: #9a1a1a;
    --ink: #2b2b2b;
    --ink-dark: #111111;
    --paper-shadow: rgba(0, 0, 0, 0.28);
  }
  * { box-sizing: border-box; margin: 0; padding: 0; }
  html, body {
    width: 1200px;
    height: 1200px;
    overflow: hidden;
    background: var(--backdrop);
    font-family: "Source Sans 3", "Myriad Pro", Arial, sans-serif;
  }
  .stage {
    position: relative;
    width: 1200px;
    height: 1200px;
  }
  .card {
    position: absolute;
    left: 239px;
    width: 722px;
    height: 412px;
    box-shadow: 0 3px 8px var(--paper-shadow);
  }
  .card--back {
    top: 162px;
    background: var(--card-black);
  }
  .card--front {
    top: 612px;
    background: var(--card-white);
  }

  /* wordmark */
  .wordmark {
    position: absolute;
    display: flex;
    align-items: center;
    gap: 14px;
  }
  .wordmark__square {
    width: 44px;
    height: 44px;
    background: var(--brand-red);
  }
  .wordmark__name {
    font-size: 38px;
    font-weight: 600;
    letter-spacing: 0.5px;
    line-height: 1;
    white-space: nowrap;
  }
  .card--back .wordmark {
    right: 18px;
    bottom: 22px;
  }
  .card--back .wordmark__name { color: var(--card-white); }
  .card--front .wordmark {
    left: 26px;
    top: 52px;
  }
  .card--front .wordmark__name { color: var(--ink-dark); }

  /* person */
  .person {
    position: absolute;
    left: 24px;
    top: 186px;
  }
  .person__name {
    color: var(--brand-red);
    font-size: 25px;
    font-weight: 700;
    text-transform: uppercase;
    letter-spacing: 0.2px;
    line-height: 1.2;
  }
  .person__title {
    color: var(--ink);
    font-size: 18px;
    margin-top: 4px;
  }

  /* contact */
  .contact {
    position: absolute;
    left: 365px;
    top: 186px;
    color: var(--ink);
    font-size: 18px;
    line-height: 1.4;
    list-style: none;
  }
  .contact__address { margin-bottom: 6px; }
  .contact__item {
    display: flex;
    align-items: center;
    gap: 9px;
    height: 32px;
  }
  .contact__icon {
    width: 23px;
    height: 23px;
    flex: none;
  }
</style>
</head>
<body>
<main class="stage">

  <section class="card card--back" aria-label="Card back">
    <div class="wordmark">
      <span class="wordmark__square"></span>
      <span class="wordmark__name">Hadley &amp; Partners</span>
    </div>
  </section>

  <section class="card card--front" aria-label="Card front">
    <div class="wordmark">
      <span class="wordmark__square"></span>
      <span class="wordmark__name">Hadley &amp; Partners</span>
    </div>

    <div class="person">
      <h1 class="person__name">Marcus J. Pellew</h1>
      <p class="person__title">President</p>
    </div>

    <ul class="contact">
      <li class="contact__address">42 W. Calloway St., Suite 300<br>Pasadena, CA 91417</li>
      <li class="contact__item">
        <svg class="contact__icon" viewBox="0 0 24 24" aria-hidden="true">
          <circle cx="12" cy="12" r="12" fill="var(--brand-red)"/>
          <path d="M8.2 6.5l2 2.3-1.1 1.4c.8 1.7 2 2.9 3.7 3.7l1.4-1.1 2.3 2-1.2 1.8c-4.3-.6-7.9-4.2-8.5-8.5z" fill="#fff"/>
        </svg>
        <span>626.555.0147 ext. 204</span>
      </li>
      <li class="contact__item">
        <svg class="contact__icon" viewBox="0 0 24 24" aria-hidden="true">
          <circle cx="12" cy="12" r="12" fill="var(--brand-red)"/>
          <rect x="8.5" y="5.5" width="7" height="13" rx="1.2" fill="none" stroke="#fff" stroke-width="1.5"/>
          <circle cx="12" cy="16.3" r="0.9" fill="#fff"/>
        </svg>
        <span>818.555.0193</span>
      </li>
      <li class="contact__item">
        <svg class="contact__icon" viewBox="0 0 24 24" aria-hidden="true">
          <circle cx="12" cy="12" r="12" fill="var(--brand-red)"/>
          <rect x="6" y="8" width="12" height="8.5" fill="#fff"/>
          <path d="M6 8l6 5 6-5" fill="none" stroke="var(--brand-red)" stroke-width="1.2"/>
        </svg>
        <span>marcus@hadleypartnersgroup.com</span>
      </li>
      <li class="contact__item">
        <svg class="contact__icon" viewBox="0 0 24 24" aria-hidden="true">
          <circle cx="12" cy="12" r="12" fill="var(--brand-red)"/>
          <circle cx="12" cy="12" r="6.3" fill="none" stroke="#fff" stroke-width="1.4"/>
          <ellipse cx="12" cy="12" rx="2.6" ry="6.3" fill="none" stroke="#fff" stroke-width="1.1"/>
          <path d="M5.8 12h12.4" stroke="#fff" stroke-width="1.1"/>
        </svg>
        <span>www.hadleypartnersgroup.com</span>
      </li>
    </ul>
  </section>

</main>
</body>
</html>
```